New Business Card for Software Company

We are looking at rebranding a 10 year old company that specializes in PDF and DWF solutions for Architects and Engineers. We will attach the new company logo that we are going with so you can work with that and complimentary colors.
The sample information we would like on the business card is:
Gerald Pembrook
Vice President
4173 W. Tillman Avenue. STE 306
PMB#417
Mesa, AZ 85316
866-392-7154 US Toll Free
123-581-3064 Cell
gpembrook@vextrolan.com
The old tag line that we had on the business cars was.
Delivering Dependable Drawing and Document Tools to Design Teams Everywhere.
If you have an idea for a better tag line we are open to that also.
Updates
We would like to thank all of the Designers for their wonderful work. We apologize that we will not have the time to provide feedback to everyone. There is just so many innovative and professional designs that you have all created making our decision even harder.
Target Market(s)
Architects and Engineers
Industry/Entity Type
Business
Look and feel
Each slider illustrates characteristics of the customer's brand and the style your logo design should communicate.

```html
<!DOCTYPE html>
<html lang="en">
<head>
<meta charset="utf-8">
<title>Vextrolan Business Card</title>
<link rel="stylesheet" href="https://fonts.googleapis.com/css2?family=Arimo:wght@400;700&display=swap">
<style>
  :root {
    --backdrop: #e6e4e1;
    --orange: #f08a1e;
    --orange-deep: #e8572a;
    --red: #d9382c;
    --ink: #4a4a4a;
    --paper: #ffffff;
    --label: #e2512a;
  }
  * { margin: 0; padding: 0; box-sizing: border-box; }
  html, body {
    width: 1200px; height: 925px; overflow: hidden;
    background: var(--backdrop);
    font-family: "Arimo", Arial, sans-serif;
  }
  .canvas { position: relative; width: 1200px; height: 925px; }
  .card {
    position: absolute; width: 600px; height: 343px; overflow: hidden;
    box-shadow: 0 8px 24px rgba(0,0,0,0.18);
  }

  /* Front */
  .card-front {
    left: 110px; top: 80px;
    background: linear-gradient(100deg, var(--red) 0%, var(--orange-deep) 45%, var(--orange) 100%);
  }
  .card-front .brand-name {
    position: absolute; right: 40px; top: 112px;
    font-weight: 700; font-size: 54px; letter-spacing: -1px; line-height: 1;
    color: var(--paper);
  }
  .card-front .tagline {
    position: absolute; left: 90px; right: 30px; top: 196px;
    font-size: 17px; line-height: 1.3; letter-spacing: 0.6px;
    color: var(--paper); text-align: right;
  }

  /* Back */
  .card-back { left: 490px; top: 500px; background: var(--paper); }
  .card-back .accent { position: absolute; inset: 0; }
  .card-back .brand {
    position: absolute; right: 40px; top: 28px;
    display: flex; align-items: center; gap: 10px;
  }
  .card-back .brand-dot {
    width: 30px; height: 30px; border-radius: 50%; background: var(--orange-deep);
  }
  .card-back .brand-name {
    font-weight: 700; font-size: 34px; letter-spacing: -0.5px; color: var(--ink);
  }
  .contact {
    position: absolute; left: 40px; top: 92px;
    color: var(--ink); font-size: 13px; letter-spacing: 1.2px; line-height: 1.45;
  }
  .contact .person-name {
    color: var(--label); font-size: 21px; letter-spacing: 0.5px; line-height: 1.1;
  }
  .contact .person-title { font-size: 13px; margin-bottom: 16px; }
  .contact .label { color: var(--label); }
  .contact .address { margin-bottom: 16px; }
</style>
</head>
<body>
<main class="canvas">

  <section class="card card-front" aria-label="Business card front">
    <div class="brand-name">Vextrolan</div>
    <p class="tagline">Delivering Dependable Drawing and Document Tools<br>to Design Teams Everywhere</p>
  </section>

  <section class="card card-back" aria-label="Business card back">
    <svg class="accent" width="600" height="343" viewBox="0 0 600 343" aria-hidden="true">
      <defs>
        <linearGradient id="accentFill" x1="0" y1="1" x2="1" y2="0">
          <stop offset="0" stop-color="#d9382c"/>
          <stop offset="0.5" stop-color="#e8572a"/>
          <stop offset="1" stop-color="#f08a1e"/>
        </linearGradient>
      </defs>
      <path d="M505 0 C420 90 320 200 250 343 L600 343 L600 0 Z" fill="url(#accentFill)"/>
    </svg>

    <div class="brand">
      <span class="brand-dot"></span>
      <span class="brand-name">Vextrolan</span>
    </div>

    <div class="contact">
      <div class="person-name">Gerald Pembrook</div>
      <div class="person-title">Vice President</div>
      <div class="label">Address :</div>
      <div class="address">4173 W. Tillman Avenue. STE 306<br>PMB#417, Mesa, AZ 85316</div>
      <div><span class="label">Tell&nbsp; :</span> 866-392-7154 US Toll Free</div>
      <div><span class="label">Cell :</span> 123-581-3064</div>
      <div><span class="label">Mail :</span> gpembrook@vextrolan.com</div>
    </div>
  </section>

</main>
</body>
</html>
```